Silver Creek Plumbing Business card & letter head design

We need a new business card and letter head for our plumbing company called silver creek plumbing. attached is the companys logo. We provide domestic and commercial plumbing services in regional western Australia. We are after Something simple yet nice to look at and something that fits within the trade industry.

Target Market(s)

trade/building industry

Contact Information for Business Card

Darl Hensby
Manager
0461 238 574
enquiries@scplumbwork.net.au
ABN: 47 381 905 462
PCL: 5187

Domestic & Commercial Plumbing
Tip Truck & Excavator hire

Colors

Designer to choose colors to be used in the design.

```html
<!DOCTYPE html>
<html lang="en">
<head>
<meta charset="utf-8">
<title>Silver Creek Plumbing – Business Card &amp; Letterhead</title>
<link href="https://fonts.googleapis.com/css2?family=Questrial&family=Open+Sans:wght@400&display=swap" rel="stylesheet">
<style>
  :root {
    --brand-blue: #1458a6;
    --ink: #4a4a4a;
    --paper: #ffffff;
    --backdrop: #e2e2e2;
    --rule: #555555;
  }
  * { box-sizing: border-box; margin: 0; padding: 0; }
  html, body { width: 1200px; height: 1017px; overflow: hidden; }
  body {
    background: var(--backdrop);
    font-family: "Questrial", sans-serif;
    color: var(--ink);
    position: relative;
  }
  .card, .letterhead { position: absolute; background: var(--paper); }
  .card { left: 78px; width: 501px; height: 285px; border-radius: 14px; }
  .card--front { top: 202px; }
  .card--back { top: 534px; background: var(--brand-blue); }

  .wordmark {
    position: absolute;
    font-family: "Questrial", sans-serif;
    color: var(--brand-blue);
    text-align: center;
    line-height: 1.05;
    letter-spacing: 0.5px;
  }
  .wordmark .line-main { display: block; }
  .wordmark .line-sub { display: block; letter-spacing: 6px; }

  .card--front .wordmark { left: 30px; width: 200px; top: 110px; font-size: 26px; }
  .card--front .wordmark .line-sub { font-size: 13px; margin-top: 4px; }

  .card--back .wordmark { left: 0; width: 501px; top: 92px; font-size: 38px; color: var(--paper); }
  .card--back .wordmark .line-sub { font-size: 18px; margin-top: 6px; }

  .divider { position: absolute; width: 1.5px; background: var(--rule); }
  .card--front .divider { left: 251px; top: 82px; height: 122px; }

  .contact { position: absolute; white-space: nowrap; }
  .contact .name { color: var(--brand-blue); text-transform: uppercase; }
  .contact p { display: flex; align-items: center; gap: 5px; }
  .contact svg { flex: none; fill: var(--brand-blue); }

  .card--front .contact { left: 271px; top: 78px; font-size: 11.5px; line-height: 15.5px; }
  .card--front .contact .name { font-size: 16.5px; line-height: 20px; }
  .card--front .contact .role { font-size: 13px; line-height: 17px; margin-bottom: 2px; }
  .card--front .contact .contact-line { margin-top: 4px; line-height: 14.5px; }
  .card--front .contact .contact-line:first-of-type { margin-top: 6px; }

  .tagline { position: absolute; left: 0; width: 100%; text-align: center; }
  .card--front .tagline { top: 245px; font-size: 12px; }
  .card--back .tagline {
    top: 223px; font-family: "Open Sans", sans-serif; font-size: 12.5px;
    line-height: 20px; color: var(--paper);
  }

  .letterhead { left: 646px; top: 167px; width: 484px; height: 683px; }
  .letterhead .wordmark { left: 22px; top: 40px; width: 180px; font-size: 22px; }
  .letterhead .wordmark .line-sub { font-size: 11px; letter-spacing: 5px; margin-top: 3px; }
  .letterhead .divider { left: 364px; top: 30px; height: 42px; background: var(--brand-blue); }
  .letterhead .contact { left: 371px; top: 27px; font-size: 8px; line-height: 10.5px; }
  .letterhead .contact .name { font-size: 11.5px; line-height: 14px; }
  .letterhead .contact .role { font-size: 9px; line-height: 11.5px; }

  .letterhead .tagline { top: 627px; font-size: 8px; }
  .letterhead .footer-rule {
    position: absolute; left: 33px; right: 34px; top: 646px; height: 1px; background: var(--brand-blue);
  }
  .footer-contacts {
    position: absolute; left: 0; width: 100%; top: 654px;
    display: flex; justify-content: center; gap: 8px; font-size: 7.5px;
  }
  .footer-contacts span { display: flex; align-items: center; gap: 3px; }
  .footer-contacts svg { fill: var(--brand-blue); }
</style>
</head>
<body>

  <section class="card card--front" aria-label="Business card front">
    <div class="wordmark"><span class="line-main">SILVER CREEK</span><span class="line-sub">PLUMBING</span></div>
    <div class="divider"></div>
    <div class="contact">
      <p class="name">Darl Hensby</p>
      <p class="role">Manager</p>
      <p>ABN: 47 381 905 462</p>
      <p>PCL: 5187</p>
      <p class="contact-line"><svg width="8" height="10" viewBox="0 0 8 10"><path d="M1 0h6a1 1 0 0 1 1 1v8a1 1 0 0 1-1 1H1a1 1 0 0 1-1-1V1a1 1 0 0 1 1-1zm.5 1.2v6.6h5V1.2z"/></svg>0461 238 574</p>
      <p class="contact-line"><svg width="9" height="7" viewBox="0 0 9 7"><path d="M0 0h9v7H0zm1 1.2v4.8h7V1.2L4.5 3.6z"/></svg>enquiries@scplumbwork.net.au</p>
      <p class="contact-line"><svg width="9" height="9" viewBox="0 0 10 10"><circle cx="5" cy="5" r="4.3" fill="none" stroke="#1458a6" stroke-width="1.2"/><path d="M3 2.5l2 1-1 2 1.5 1.5-.5 2-2-2.5zM6.5 2l1.5 1.5-1 1z"/></svg>www.scplumbwork.net.au</p>
    </div>
    <p class="tagline">Domestic &amp; Commercial Plumbing Tip Truck &amp; Excavator hire</p>
  </section>

  <section class="card card--back" aria-label="Business card back">
    <div class="wordmark"><span class="line-main">SILVER CREEK</span><span class="line-sub">PLUMBING</span></div>
    <p class="tagline">Domestic &amp; Commercial Plumbing<br>Tip Truck &amp; Excavator hire</p>
  </section>

  <section class="letterhead" aria-label="Letterhead">
    <div class="wordmark"><span class="line-main">SILVER CREEK</span><span class="line-sub">PLUMBING</span></div>
    <div class="divider"></div>
    <div class="contact">
      <p class="name">Darl Hensby</p>
      <p class="role">Manager</p>
      <p>ABN: 47 381 905 462</p>
      <p>PCL: 5187</p>
    </div>
    <p class="tagline">Domestic &amp; Commercial Plumbing Tip Truck &amp; Excavator hire</p>
    <div class="footer-rule"></div>
    <div class="footer-contacts">
      <span><svg width="5" height="7" viewBox="0 0 8 10"><path d="M1 0h6a1 1 0 0 1 1 1v8a1 1 0 0 1-1 1H1a1 1 0 0 1-1-1V1a1 1 0 0 1 1-1zm.5 1.2v6.6h5V1.2z"/></svg>0461 238 574</span>
      <span><svg width="6" height="5" viewBox="0 0 9 7"><path d="M0 0h9v7H0zm1 1.2v4.8h7V1.2L4.5 3.6z"/></svg>enquiries@scplumbwork.net.au</span>
      <span><svg width="6" height="6" viewBox="0 0 10 10"><circle cx="5" cy="5" r="4.3" fill="none" stroke="#1458a6" stroke-width="1.4"/><path d="M3 2.5l2 1-1 2 1.5 1.5-.5 2-2-2.5z"/></svg>www.scplumbwork.net.au</span>
    </div>
  </section>

</body>
</html>
```